Pale Harbor - post rock band album cover design

We are Pale Harbor, a post-rock band based on San Jose, CA, USA. We will release a new album “Where the rivers fold" and need a album cover.

The new album is full of emotion and energy. song list:
1. Forward
2. Search (in uploaded files)
3. Before
4. Memory
5. Dream
6. Spring
7. Om Namah Shivaya

Please hear our previous music here
https://pale-harbor.tunecrate-demo.net/album/pale-harbor

Target Market(s)

music lovers

Industry/Entity Type

Music Download

Colors

Requirements
Must have
• album cover + back
• For cover we only need band name (do not need album name), want to use some streamline font for the band name "Pale Harbor"
• I attached an example from another band
Nice to have
• I don't want to limit the designers, so please listen to the music and design what you feel the best:)

```html
<!DOCTYPE html>
<html lang="en">
<head>
<meta charset="utf-8">
<title>Pale Harbor — Album Cover</title>
<link rel="stylesheet" href="https://fonts.googleapis.com/css2?family=Mrs+Saint+Delafield&display=swap">
<style>
  :root {
    --page: #ffffff;
    --ink: #0c0c0c;
    --frame: #ffffff;
    --navy: #221c55;
    --green: #6cc04a;
    --green-deep: #3cb54a;
    --red: #ea2d2e;
    --rust: #b5663a;
    --black: #070707;
  }
  * { margin: 0; padding: 0; box-sizing: border-box; }
  html, body {
    width: 1199px;
    height: 1200px;
    overflow: hidden;
    background: var(--page);
  }
  .canvas {
    position: relative;
    width: 1199px;
    height: 1200px;
    background: var(--page);
  }
  .cover {
    position: absolute;
    left: 199px;
    top: 191px;
    width: 831px;
    height: 831px;
    overflow: visible;
  }
  .cover-art {
    position: absolute;
    inset: 0;
    width: 831px;
    height: 831px;
    display: block;
  }
  .name-frame {
    position: absolute;
    left: 90px;
    top: 340px;
    width: 652px;
    height: 125px;
    border: 2px solid var(--frame);
  }
  .band-name {
    position: absolute;
    left: 100px;
    top: 318px;
    width: 700px;
    font-family: "Mrs Saint Delafield", cursive;
    font-weight: 400;
    font-size: 118px;
    line-height: 1.3;
    color: var(--ink);
    white-space: nowrap;
  }
</style>
</head>
<body>
  <main class="canvas">
    <section class="cover">
      <svg class="cover-art" role="img" aria-label="Abstract flowing light bands in navy, green and red" viewBox="0 0 831 831" xmlns="http://www.w3.org/2000/svg">
        <defs>
          <linearGradient id="flow" x1="0" y1="0" x2="0" y2="1">
            <stop offset="0" stop-color="var(--navy)"/>
            <stop offset="0.07" stop-color="#2a7c4b"/>
            <stop offset="0.16" stop-color="var(--green-deep)"/>
            <stop offset="0.3" stop-color="var(--green)"/>
            <stop offset="0.4" stop-color="#62bb47"/>
            <stop offset="0.47" stop-color="var(--rust)"/>
            <stop offset="0.58" stop-color="var(--red)"/>
            <stop offset="0.7" stop-color="#d24a33"/>
            <stop offset="0.78" stop-color="var(--green)"/>
            <stop offset="0.88" stop-color="var(--green-deep)"/>
            <stop offset="0.95" stop-color="var(--navy)"/>
            <stop offset="1" stop-color="var(--black)"/>
          </linearGradient>
          <radialGradient id="navy-top" cx="0.55" cy="0.05" r="0.35">
            <stop offset="0" stop-color="var(--navy)"/>
            <stop offset="1" stop-color="var(--navy)" stop-opacity="0"/>
          </radialGradient>
          <radialGradient id="red-right" cx="0.9" cy="0.7" r="0.3">
            <stop offset="0" stop-color="var(--red)"/>
            <stop offset="1" stop-color="var(--red)" stop-opacity="0"/>
          </radialGradient>
        </defs>
        <rect width="831" height="831" fill="url(#flow)"/>
        <rect width="831" height="831" fill="url(#navy-top)"/>
        <rect width="831" height="831" fill="url(#red-right)"/>
      </svg>
      <div class="name-frame"></div>
      <h1 class="band-name">Pale Harbor</h1>
    </section>
  </main>
</body>
</html>
```